Marketing One-Sheet for Security Deposit Claim Notice

I need a one-sheet flyer formatted for email distribution — optimized as a JPEG/PNG that I can insert into Constant Contact or Outlook. I do not want to attach it to an email, but insert it in the email we send out. I would like it to look professional but engaging. Some images would be good, but want to make sure it reads well if images do not load for the recipients. The text is in the attached Word document, but I am open to changes/ideas that may be better for marketing purposes. I included the URLs for some of the links I would like in the one-sheet that is clickable. The logo for the business is being uploaded on the Word document. Proposed text is also uploaded in a Word document. Thank you.

Target Market(s)

Landlords, Real Estate Agents, Property Managers

Industry/Entity Type

Legal

Requirements
Must have
• Professional but appealing design. The One-sheet is going to be placed in the body of emails, not as an attachment.
Nice to have
• Include our logo for the business and the web links please.
Should not have
• Images can be ok, but it needs to look right if images do not download from the email sent out.

```html
<!DOCTYPE html>
<html lang="en">
<head>
<meta charset="utf-8">
<title>Tenancy Counsel Group – Security Deposit Claim Notices</title>
<link href="https://fonts.googleapis.com/css2?family=Open+Sans:wght@400;600;700;800&family=Tinos:wght@400;700&display=swap" rel="stylesheet">
<style>
  :root {
    --red: #e3201b;
    --red-bright: #f0231e;
    --red-deep: #8c0f0f;
    --maroon: #6b0a06;
    --ink: #111111;
    --white: #ffffff;
    --rule: #b5776f;
    --photo-dark: #3a3430;
    --photo-light: #c9c1b6;
  }
  html, body {
    margin: 0;
    padding: 0;
    overflow: hidden;
    background: var(--white);
  }
  .sheet {
    position: relative;
    width: 1200px;
    height: 2400px;
    overflow: hidden;
    background: var(--white);
    font-family: "Open Sans", Arial, sans-serif;
    color: var(--ink);
  }
  .hero-art {
    position: absolute;
    left: 0;
    top: 0;
    width: 1200px;
    height: 790px;
  }
  .brand {
    position: absolute;
    left: 64px;
    top: 104px;
    display: flex;
    align-items: center;
    gap: 18px;
  }
  .brand-name {
    font-family: "Tinos", "Times New Roman", serif;
    font-weight: 400;
    font-size: 46px;
    line-height: 48px;
    color: var(--red-deep);
    letter-spacing: 1px;
  }
  .brand-mark {
    width: 34px;
    height: 34px;
    background: var(--red-deep);
  }
  .headline {
    position: absolute;
    left: 66px;
    top: 356px;
    margin: 0;
    font-weight: 800;
    font-size: 70px;
    line-height: 90px;
    color: var(--white);
    letter-spacing: 1px;
  }
  .benefits {
    position: absolute;
    left: 66px;
    top: 712px;
    width: 1000px;
  }
  .benefits-title {
    margin: 0 0 6px;
    font-weight: 700;
    font-size: 32px;
    line-height: 46px;
  }
  .check-list {
    list-style: none;
    margin: 0;
    padding: 0;
  }
  .check-list li {
    position: relative;
    padding-left: 58px;
    font-size: 33px;
    line-height: 53px;
  }
  .check-list li::before {
    content: "✓";
    position: absolute;
    left: 0;
    top: 0;
    font-size: 30px;
  }
  .price-tag {
    position: absolute;
    left: 306px;
    top: 958px;
    width: 584px;
    height: 96px;
    background: var(--red);
    color: var(--white);
    font-family: "Tinos", "Times New Roman", serif;
    font-size: 72px;
    line-height: 96px;
    text-align: center;
  }
  .price-note {
    position: absolute;
    left: 0;
    top: 1068px;
    width: 1200px;
    text-align: center;
    font-weight: 700;
    font-size: 30px;
    line-height: 42px;
  }
  .warning {
    position: absolute;
    left: 66px;
    top: 1134px;
    width: 1100px;
  }
  .warning-lead {
    margin: 0 0 4px;
    font-size: 32px;
    line-height: 50px;
  }
  .warning-lead u {
    font-style: italic;
  }
  .divider {
    position: absolute;
    left: 66px;
    top: 1402px;
    width: 1044px;
    height: 2px;
    background: var(--rule);
  }
  .explainer {
    position: absolute;
    left: 74px;
    top: 1430px;
    width: 1040px;
    margin: 0;
    font-size: 31px;
    line-height: 52px;
  }
  .commercial-box {
    position: absolute;
    left: 266px;
    top: 1744px;
    width: 662px;
    height: 142px;
    border: 4px solid var(--red);
    box-sizing: border-box;
    display: flex;
    align-items: center;
    justify-content: center;
    text-align: center;
    font-family: "Tinos", "Times New Roman", serif;
    font-weight: 700;
    font-size: 46px;
    line-height: 56px;
  }
  .commercial-box .amount {
    color: var(--red);
    font-weight: 400;
  }
  .cta {
    position: absolute;
    left: 0;
    top: 1912px;
    width: 1200px;
    margin: 0;
    text-align: center;
    font-weight: 700;
    font-size: 39px;
    line-height: 58px;
    color: var(--red-deep);
  }
  .footer {
    position: absolute;
    left: 0;
    top: 2062px;
    width: 1200px;
    height: 338px;
    background: var(--maroon);
    color: var(--white);
    text-align: center;
  }
  .footer-name {
    position: absolute;
    top: 34px;
    width: 100%;
    font-size: 32px;
    line-height: 44px;
    letter-spacing: 1px;
  }
  .footer-phone {
    position: absolute;
    top: 82px;
    width: 100%;
    font-weight: 700;
    font-size: 60px;
    line-height: 80px;
  }
  .footer-web {
    position: absolute;
    top: 162px;
    width: 100%;
    font-size: 34px;
    line-height: 46px;
    letter-spacing: 5px;
  }
  .more-button {
    position: absolute;
    left: 318px;
    top: 224px;
    width: 564px;
    height: 68px;
    border-radius: 24px;
    background: var(--red-bright);
    font-family: "Tinos", "Times New Roman", serif;
    font-weight: 700;
    font-size: 32px;
    line-height: 68px;
    color: var(--white);
    text-decoration: none;
  }
</style>
</head>
<body>
<main class="sheet">
  <svg class="hero-art" viewBox="0 0 1200 790" xmlns="http://www.w3.org/2000/svg">
    <defs>
      <linearGradient id="bannerFill" x1="0" y1="0" x2="1" y2="0">
        <stop offset="0" stop-color="#8c0f0f"/>
        <stop offset="0.55" stop-color="#c8161a"/>
        <stop offset="1" stop-color="#ef231e"/>
      </linearGradient>
      <linearGradient id="photoFill" x1="0" y1="0" x2="1" y2="1">
        <stop offset="0" stop-color="#cfc7bc"/>
        <stop offset="0.5" stop-color="#8a7f74"/>
        <stop offset="1" stop-color="#3a3430"/>
      </linearGradient>
    </defs>
    <polygon role="img" aria-label="Photo of a lawyer at a desk with a judge's gavel and documents"
             points="720,0 1200,0 1200,690 940,690 600,300" fill="url(#photoFill)"/>
    <polygon points="690,0 748,0 598,300 540,300" fill="#a3120f"/>
    <polygon points="0,300 720,300 940,690 0,690" fill="url(#bannerFill)"/>
    <polygon points="720,690 940,690 720,762" fill="#111111"/>
    <polyline points="812,722 812,776 1200,776" fill="none" stroke="#e3201b" stroke-width="4"/>
  </svg>

  <div class="brand">
    <span class="brand-name">TENANCY COUNSEL<br>GROUP</span>
    <span class="brand-mark"></span>
  </div>

  <h1 class="headline">WE PREPARE<br>SECURITY DEPOSIT<br>CLAIM NOTICES</h1>

  <section class="benefits">
    <p class="benefits-title">Keep the tenant’s Security Deposit</p>
    <ul class="check-list">
      <li>Cover unpaid Rent</li>
      <li>Apply to legal fees and costs</li>
      <li>Charge against Damages to the Property</li>
    </ul>
  </section>

  <div class="price-tag">FLAT FEE $350</div>
  <p class="price-note" style="margin:0">Follow Florida law to keep the Deposit</p>

  <section class="warning">
    <p class="warning-lead">If the Security Deposit Claim is not made <u>correctly</u> <strong>and</strong> <u>on time</u>, then:</p>
    <ul class="check-list">
      <li>Tenant is automatically entitled to their full deposit back</li>
      <li>No claim against the deposit can be made</li>
      <li>Tenant can sue and recover the deposit and thousands in legal</li>
    </ul>
  </section>

  <div class="divider"></div>

  <p class="explainer">Lawyers often focus on helping tenants, and they actively pursue landlords who fail to correctly process security deposit claims. If a claim is handled improperly, these lawyers can sue the landlord, win the case, and make the landlord pay thousands of dollars in legal fees—even if the tenant actually owes back rent.</p>

  <div class="commercial-box">
    <span>For commercial properties,<br>the flat legal fee is <span class="amount">$450</span></span>
  </div>

  <p class="cta">Hire Us to prepare and serve to the tenant<br>the security deposit claim</p>

  <footer class="footer">
    <div class="footer-name">TENANCY COUNSEL GROUP</div>
    <div class="footer-phone">1-800-555-0142</div>
    <div class="footer-web">TenancyCounselGroup.com</div>
    <a class="more-button" href="#">Click here for more information</a>
  </footer>
</main>
</body>
</html>
```